Tobias Wrenfield - Cinematographer

NEED:
I'm looking for a sleek, professional, modern business card that will give give the recipient the impression that they can trust their production will go smoothly by hiring me. I will bring creativity and knowledge to their shoot, so that we can create powerful images.
I am looking for a card with a strong style and design ethos that could be expanded to a website and a full visual/graphic/design entity for me.
ABOUT ME:
I am a mid-twenties cinematographer, I work on music video, narrative short, commercial, and corporate projects. I blend the science and artistry of cameras and filmmaking to tell a story. I'm an artist, a technician, and a manager.
DESIGN:
I like sleek, simple design. Black, dark grays, white, dark navy, steel blues, I love cyan, but also cyan and red. I am not a fan of earthy tones. I generally prefer modern, san-serif fonts over serifs. My old logo was based on an aperture, a multi-blade device at the back of a lens that controls how much light passes through, but I made it with so many colors, that it doesn't necessarily lend itself to a specific color-scheme or design ethos. I liked that the aperture design provided a sense of the technical requirements of my job. I'm a fan of matte business cards, but am open to plenty of specialty print processes to make an outstanding card.
ATTACHED FILES:
My Old Rainbox Aperture Logo, plus a few designs I've tried playing around with, but am not tied to. I AM OPEN TO NEW DESIGNS, DO NOT FEEL TIED TO THIS.
**I've pulled my old logo down from the attached files, and instead attached other business cards I like, so as not to mislead you where I would like to go.
INFO:
Name: Tobias Wrenfield
Job: Cinematographer
Email: tkwrenfield@quillbox.example
Phone: 503.618.2907
Website: tobiaswrenfield.example
Updates
I'm adding some images of other cards that I like, and removing my old logo, since I'm looking for something new, and don't want that old logo to push anyone a certain direction.

```html
<!DOCTYPE html>
<html lang="en">
<head>
<meta charset="utf-8">
<title>Tobias Wrenfield – Cinematographer Business Card</title>
<link rel="stylesheet" href="https://fonts.googleapis.com/css2?family=Advent+Pro:wght@200;300;400&display=swap">
<style>
  :root {
    --backdrop-center: #eef8f8;
    --backdrop-edge: #c8e7e4;
    --card-black: #231f20;
    --lens-gray: #302c2c;
    --shadow-gray: #5a5a5a;
    --line-ice: #d9f1ef;
    --ink-white: #ffffff;
    --accent-cyan: #6ccbc2;
    --accent-red: #e8483a;
  }
  * { margin: 0; padding: 0; box-sizing: border-box; }
  html, body {
    width: 1200px; height: 900px; overflow: hidden;
  }
  body {
    position: relative;
    background: radial-gradient(circle at 50% 50%, var(--backdrop-center) 0%, var(--backdrop-edge) 100%);
    font-family: "Advent Pro", "Arial Narrow", sans-serif;
  }
  .card-art { position: absolute; inset: 0; width: 1200px; height: 900px; }
  .card-back { fill: var(--card-black); }
  .card-shadow { fill: var(--shadow-gray); }
  .lens-inner { fill: var(--lens-gray); stroke: var(--line-ice); stroke-width: 1.6; }
  .lens-outer { fill: none; stroke: var(--line-ice); stroke-width: 1.6; }
  .crosshair { stroke: var(--line-ice); stroke-width: 3.2; }
  .crosshair-bright { stroke: var(--ink-white); stroke-width: 3.2; }
  .mark-square { fill: var(--accent-red); }

  .front-name {
    position: absolute; left: 296px; top: 678px;
    font-weight: 300; font-size: 34px; letter-spacing: 0.5px;
    color: var(--ink-white); text-transform: uppercase; line-height: 1;
    white-space: nowrap;
  }

  .identity {
    position: absolute; left: 638px; top: 160px;
    width: 360px;
    transform: rotate(-4deg); transform-origin: left top;
    text-transform: uppercase; line-height: 1;
  }
  .identity-name { color: var(--ink-white); font-weight: 300; white-space: nowrap; }
  .identity-first { font-size: 46px; }
  .identity-last { font-size: 30px; }
  .identity-role {
    color: var(--accent-cyan); font-weight: 300; font-size: 47px;
    margin-top: 6px; white-space: nowrap;
  }

  .contact {
    position: absolute; right: 210px; top: 604px;
    transform: rotate(-4deg); transform-origin: right top;
    text-align: right; list-style: none;
    color: var(--ink-white); font-weight: 300; font-size: 22px;
    text-transform: uppercase; line-height: 34px;
    white-space: nowrap;
  }
</style>
</head>
<body>
  <svg class="card-art" viewBox="0 0 1200 900" aria-hidden="true">
    <defs>
      <clipPath id="clip-front"><rect x="180" y="117" width="412" height="666"/></clipPath>
      <clipPath id="clip-back"><rect x="610" y="117" width="410" height="666"/></clipPath>
    </defs>

    <rect class="card-shadow" x="188" y="125" width="412" height="666"/>
    <rect class="card-shadow" x="618" y="125" width="410" height="666"/>

    <g class="card card-front" clip-path="url(#clip-front)">
      <rect class="card-back" x="180" y="117" width="412" height="666"/>
      <circle class="lens-outer" cx="439" cy="611" r="364"/>
      <circle class="lens-inner" cx="445" cy="640" r="290"/>
      <line class="crosshair" x1="357" y1="100" x2="455" y2="800"/>
      <line class="crosshair" x1="60" y1="662" x2="1100" y2="514"/>
      <rect class="mark-square" x="250" y="680" width="34" height="34"/>
    </g>

    <g class="card card-reverse" clip-path="url(#clip-back)">
      <rect class="card-back" x="610" y="117" width="410" height="666"/>
      <circle class="lens-outer" cx="439" cy="611" r="364"/>
      <circle class="lens-inner" cx="445" cy="640" r="290"/>
      <line class="crosshair-bright" x1="60" y1="662" x2="1100" y2="514"/>
    </g>
  </svg>

  <div class="front-name">Tobias Wrenfield</div>

  <header class="identity">
    <div class="identity-name"><span class="identity-first">Tobias</span><span class="identity-last"> Wrenfield</span></div>
    <div class="identity-role">Cinematographer</div>
  </header>

  <ul class="contact">
    <li class="contact-phone">503.618.2907</li>
    <li class="contact-web">tobiaswrenfield.example</li>
    <li class="contact-email">tkwrenfield@quillbox.example</li>
  </ul>
</body>
</html>
```